UX/UI Design of mobile application for language learning through picture cards

We are looking for a Mobile Application Designer with knowledge of UX/UI concepts.

We best candidate is a skilled Mobile Application Designer with knowledge of last trends and with experience in completing similar tasks.

This is a test task. After successful completion, the best candidate will be given a full task.

```html
<!DOCTYPE html>
<html lang="en">
<head>
<meta charset="utf-8">
<title>Cardo Lingo – Picture Quiz</title>
<link rel="stylesheet" href="https://fonts.googleapis.com/css2?family=Montserrat:wght@600;700&family=Open+Sans:wght@400;600;700&display=swap">
<style>
  :root {
    --page-bg: #f1efee;
    --screen-bg: #ffffff;
    --ink: #111111;
    --muted: #8c8c8c;
    --label: #4a4a4a;
    --brand: #ef5a36;
    --orange: #ff8412;
    --orange-dark: #b95a0d;
    --stack-1: #fde6d8;
    --stack-2: #fec896;
    --stack-3: #fba863;
    --option-border: #d4d4d4;
    --divider: #cfcfcf;
    --success: #8db600;
    --button: #453b3a;
    --frame-active: #f00000;
    --frame-idle: #a2a2a2;
  }
  * { box-sizing: border-box; margin: 0; padding: 0; }
  html, body {
    width: 1077px; height: 1200px; overflow: hidden;
    background: var(--page-bg);
    font-family: "Open Sans", Arial, sans-serif;
    color: var(--ink);
  }
  .app-screen {
    position: absolute; left: 267px; top: 12px;
    width: 418px; height: 904px;
    transform: scale(1.3); transform-origin: top left;
    background: var(--screen-bg);
    border-radius: 34px; overflow: hidden;
    box-shadow: 0 10px 30px rgba(0,0,0,0.08);
  }
  .status-bar { position: absolute; left: 0; top: 16px; width: 100%; height: 20px; }
  .status-time { position: absolute; left: 20px; top: 0; font-size: 15px; font-weight: 600; }
  .status-icons { position: absolute; right: 22px; top: 3px; }

  .app-header { position: absolute; left: 20px; top: 50px; width: 378px; height: 34px; }
  .brand { display: flex; align-items: center; gap: 7px; height: 34px; }
  .brand-mark { width: 14px; height: 14px; background: var(--brand); border-radius: 3px; }
  .brand-name { font-family: "Montserrat", Arial, sans-serif; font-weight: 700; font-size: 18px; color: var(--ink); }
  .menu-icon { position: absolute; right: 0; top: 13px; }

  .card-stack span { position: absolute; border-radius: 4px 4px 0 0; }
  .stack-back { left: 61px; top: 107px; width: 296px; height: 20px; background: var(--stack-1); }
  .stack-mid { left: 47px; top: 121px; width: 324px; height: 20px; background: var(--stack-2); }
  .stack-front { left: 33px; top: 134px; width: 352px; height: 20px; background: var(--stack-3); }

  .picture-card {
    position: absolute; left: 20px; top: 148px; width: 378px; height: 446px;
    border-radius: 4px; overflow: hidden;
    background:
      radial-gradient(ellipse at 55% 60%, #b59c7f 0 18%, rgba(181,156,127,0) 40%),
      radial-gradient(ellipse at 75% 12%, #f2e3b5 0 10%, rgba(242,227,181,0) 35%),
      linear-gradient(180deg, #8f8a4f 0%, #5f6a33 45%, #6f7a3a 75%, #8b9343 100%);
    box-shadow: 0 2px 6px rgba(0,0,0,0.15);
  }
  .highlight { position: absolute; }
  .highlight-idle { left: 67px; top: 4px; width: 305px; height: 79px; border: 2px solid var(--frame-idle); }
  .highlight-active { left: 18px; top: 92px; width: 306px; height: 354px; border: 3px solid var(--frame-active); }

  .question {
    position: absolute; left: 20px; top: 612px;
    font-family: "Montserrat", Arial, sans-serif; font-weight: 700; font-size: 17px;
  }
  .answer {
    position: absolute; width: 182px; height: 46px;
    border: 1px solid var(--option-border); border-radius: 23px;
    display: flex; align-items: center; font-size: 15px;
  }
  .answer-key {
    width: 48px; height: 48px; margin: -1px 0 0 -2px; border-radius: 50%;
    background: var(--orange); color: #fff; font-weight: 700; font-size: 16px;
    display: flex; align-items: center; justify-content: center;
  }
  .answer-text { margin-left: 19px; }
  .answer-a { left: 19px; top: 655px; }
  .answer-b { left: 217px; top: 655px; }
  .answer-c { left: 19px; top: 719px; background: var(--orange); border-color: var(--orange); color: #fff; font-weight: 600; }
  .answer-c .answer-key { background: var(--orange-dark); }
  .answer-d { left: 217px; top: 719px; }

  .divider { position: absolute; left: 19px; top: 783px; width: 380px; height: 1px; background: var(--divider); }
  .progress { position: absolute; left: 19px; top: 804px; font-size: 15px; font-weight: 600; color: var(--label); }
  .progress-count { color: var(--muted); font-weight: 700; margin-left: 4px; }
  .result { position: absolute; right: 20px; top: 797px; display: flex; align-items: center; gap: 10px;
    color: var(--success); font-weight: 700; font-size: 15px; }

  .next-button {
    position: absolute; left: 19px; top: 841px; width: 380px; height: 49px;
    border-radius: 25px; background: var(--button); color: #fff;
    display: flex; align-items: center; justify-content: center; gap: 12px;
    font-weight: 700; font-size: 17px;
  }
</style>
</head>
<body>
  <main class="app-screen">
    <div class="status-bar">
      <span class="status-time">9:41</span>
      <svg class="status-icons" width="68" height="12" viewBox="0 0 68 12">
        <rect x="0" y="8" width="3" height="4" rx="1" fill="#111"/>
        <rect x="4.5" y="6" width="3" height="6" rx="1" fill="#111"/>
        <rect x="9" y="3.5" width="3" height="8.5" rx="1" fill="#111"/>
        <rect x="13.5" y="1" width="3" height="11" rx="1" fill="#111"/>
        <path d="M22 4.5a10 10 0 0 1 14 0l-1.5 1.5a8 8 0 0 0-11 0z M25 7.5a6 6 0 0 1 8 0l-1.5 1.5a4 4 0 0 0-5 0z M27.5 10a2 2 0 0 1 3 0L29 11.5z" fill="#111"/>
        <rect x="42" y="1" width="22" height="10.5" rx="3" fill="none" stroke="#111" stroke-opacity="0.45"/>
        <rect x="44" y="3" width="18" height="6.5" rx="1.5" fill="#111"/>
        <rect x="65" y="4.5" width="1.6" height="3.5" rx="0.8" fill="#111" fill-opacity="0.45"/>
      </svg>
    </div>

    <header class="app-header">
      <div class="brand">
        <span class="brand-mark"></span>
        <span class="brand-name">Cardo Lingo</span>
      </div>
      <svg class="menu-icon" width="19" height="12" viewBox="0 0 19 12">
        <rect x="0" y="0" width="19" height="1.8" fill="#111"/>
        <rect x="0" y="5" width="15" height="1.8" fill="#111"/>
        <rect x="0" y="10" width="10" height="1.8" fill="#111"/>
      </svg>
    </header>

    <div class="card-stack">
      <span class="stack-back"></span>
      <span class="stack-mid"></span>
      <span class="stack-front"></span>
    </div>

    <section class="picture-card" role="img" aria-label="Photo of a deer with antlers standing on a sunlit meadow in front of trees">
      <div class="highlight highlight-idle"></div>
      <div class="highlight highlight-active"></div>
    </section>

    <h2 class="question">What is highlighted in the picture?</h2>

    <div class="answer answer-a"><span class="answer-key">A</span><span class="answer-text">Giraffe</span></div>
    <div class="answer answer-b"><span class="answer-key">B</span><span class="answer-text">Bear</span></div>
    <div class="answer answer-c"><span class="answer-key">C</span><span class="answer-text">Deer</span></div>
    <div class="answer answer-d"><span class="answer-key">D</span><span class="answer-text">Tree</span></div>

    <div class="divider"></div>

    <p class="progress">Object:<span class="progress-count">1/2</span></p>
    <p class="result">
      <svg width="31" height="31" viewBox="0 0 31 31">
        <circle cx="15.5" cy="15.5" r="15.5" fill="#8db600"/>
        <path d="M9 16l4.5 4.5L22.5 11" fill="none" stroke="#fff" stroke-width="2.4" stroke-linecap="round" stroke-linejoin="round"/>
      </svg>
      Correct
    </p>

    <div class="next-button">
      Next Picture
      <svg width="20" height="12" viewBox="0 0 20 12">
        <path d="M1 6h17M13 1.5L18 6l-5 4.5" fill="none" stroke="#fff" stroke-width="1.6" stroke-linecap="round" stroke-linejoin="round"/>
      </svg>
    </div>
  </main>
</body>
</html>
```